Package design for small honey and vegetable farm

I would like to have a unique design for the packaging of our honey and vegetables. I have attached the logo from our farm "Willowbrook Acres" that should be on the packaging for both the honey and the vegetables

For the honey the writing, "100% pure organic honey" must be on the packaging in some place. As well as "from the busy bees at Willowbrook Acres". I have attached some designs that I like.

For the vegetables. The design will need to go on a box like the one in the attached image. The phrase "Organically Grown" should be on the package. I would like the background color of the package to be black. I think I would also like to see some stylized vegetables (tomatoes in particular) on the package.

I would like to be able to get all the colors (RGB) used in the designs so I can pass them on to printers.

Industry/Entity Type

Farm

Colors
fbee3e

Requirements
Must have
• For the honey, the package it must say "100% pure organic honey".
• For the vegetables I would like the background color to be black. I would also like some stylized vegetables (tomatoes in particular) added to the package.

```html
<!DOCTYPE html>
<html lang="en">
<head>
<meta charset="utf-8">
<title>Willowbrook Acres – Honey Bottles</title>
<link rel="stylesheet" href="https://fonts.googleapis.com/css2?family=Josefin+Sans:wght@400;600&display=swap">
<style>
  :root {
    --backdrop: #f3f5f5;
    --cap: #1e1f1f;
    --cap-edge: #2c2d2d;
    --amber-light: #c7841a;
    --amber-mid: #a8640f;
    --amber-deep: #6f4a10;
    --olive-light: #b89a1c;
    --olive-deep: #8f7c18;
    --gold-ink: #f0c81e;
    --cream-ink: #f6eed8;
    --white-ink: #f8f5ee;
  }
  * { margin: 0; padding: 0; box-sizing: border-box; }
  html, body { width: 1200px; height: 675px; overflow: hidden; background: var(--backdrop); }
  .canvas {
    position: relative;
    width: 1200px;
    height: 675px;
    background: var(--backdrop);
    font-family: "Josefin Sans", sans-serif;
  }
  .bottles { position: absolute; inset: 0; }
  .label {
    position: absolute;
    width: 220px;
    display: flex;
    flex-direction: column;
    align-items: center;
    text-align: center;
  }
  .label--amber { left: 283px; top: 352px; }
  .label--olive { left: 675px; top: 374px; }
  .brand {
    display: flex;
    flex-direction: column;
    align-items: center;
    font-weight: 600;
    font-size: 24px;
    line-height: 1.08;
    letter-spacing: 0.4px;
  }
  .label--amber .brand { color: var(--gold-ink); }
  .label--olive .brand { color: var(--white-ink); }
  .product-name {
    margin-top: 56px;
    font-size: 9.4px;
    letter-spacing: 1.5px;
    text-transform: uppercase;
    white-space: nowrap;
  }
  .label--amber .product-name,
  .label--amber .tagline { color: var(--cream-ink); }
  .label--olive .product-name,
  .label--olive .tagline { color: var(--white-ink); }
  .divider-dot {
    width: 6px; height: 6px; border-radius: 50%;
    margin: 8px 0 7px;
  }
  .label--amber .divider-dot { background: var(--gold-ink); }
  .label--olive .divider-dot { background: var(--white-ink); }
  .tagline {
    font-size: 4.8px;
    letter-spacing: 0.5px;
    text-transform: uppercase;
    white-space: nowrap;
  }
</style>
</head>
<body>
  <main class="canvas">
    <svg class="bottles" viewBox="0 0 1200 675" width="1200" height="675" aria-hidden="true">
      <defs>
        <radialGradient id="amberGlass" cx="50%" cy="40%" r="65%">
          <stop offset="0" stop-color="var(--amber-light)"/>
          <stop offset="0.6" stop-color="var(--amber-mid)"/>
          <stop offset="1" stop-color="var(--amber-deep)"/>
        </radialGradient>
        <linearGradient id="oliveGlass" x1="0" y1="0" x2="0" y2="1">
          <stop offset="0" stop-color="var(--amber-mid)"/>
          <stop offset="0.45" stop-color="var(--olive-light)"/>
          <stop offset="1" stop-color="var(--olive-deep)"/>
        </linearGradient>
      </defs>

      <!-- amber bottle -->
      <g class="bottle bottle--amber">
        <rect x="340" y="200" width="108" height="80" rx="32" fill="var(--amber-mid)"/>
        <path d="M282 296 Q282 256 322 256 L464 256 Q504 256 504 296 L504 572 Q504 592 484 592 L302 592 Q282 592 282 572 Z" fill="url(#amberGlass)"/>
        <rect x="358" y="156" width="70" height="90" fill="var(--cap)"/>
        <rect x="350" y="142" width="86" height="14" rx="2" fill="var(--cap-edge)"/>
        <rect x="366" y="128" width="54" height="14" fill="var(--cap)"/>
        <path d="M328 128 L328 112 Q328 92 360 92 L426 92 Q458 92 458 112 L458 128 Z" fill="var(--cap)"/>
      </g>

      <!-- olive bottle -->
      <g class="bottle bottle--olive">
        <path d="M682 340 Q682 276 746 276 L824 276 Q888 276 888 340 L888 576 Q888 594 870 594 L700 594 Q682 594 682 576 Z" fill="url(#oliveGlass)"/>
        <rect x="746" y="192" width="82" height="84" fill="var(--cap)"/>
        <rect x="734" y="176" width="102" height="16" rx="2" fill="var(--cap-edge)"/>
        <rect x="760" y="152" width="52" height="24" fill="var(--cap)"/>
        <rect x="724" y="138" width="118" height="14" rx="3" fill="var(--cap)"/>
        <path d="M728 140 L726 192 L732 196" fill="none" stroke="var(--cap)" stroke-width="1.5"/>
        <path d="M838 140 L864 154 L886 178" fill="none" stroke="var(--cap)" stroke-width="1.5"/>
      </g>
    </svg>

    <section class="label label--amber" aria-label="Honey label, gold lettering">
      <div class="brand"><span>Willowbrook</span><span>Acres</span></div>
      <p class="product-name">100% Pure Organic Honey</p>
      <span class="divider-dot"></span>
      <p class="tagline">From the busy bees at Willowbrook Acres</p>
    </section>

    <section class="label label--olive" aria-label="Honey label, white lettering">
      <div class="brand"><span>Willowbrook</span><span>Acres</span></div>
      <p class="product-name">100% Pure Organic Honey</p>
      <span class="divider-dot"></span>
      <p class="tagline">From the busy bees at Willowbrook Acres</p>
    </section>
  </main>
</body>
</html>
```